New Template design for Website in Wordpress

We are interested in changing our website look at www.cargolinx.com -We also are very interested in Have it done in Wordpress in which we are understanding the search engines are liking a bit more. The website we would want to try working with on this is www.cargolinx.com. We look forward to seeing the different design ideas please just make sure they are in wordpress! Thanks, Marlen

Reason: need more design idea..... We would still like to use our pictures off our site since we paid for them so keep that in mind as well as we would still want the rotating pictures in the head of the page but not in Flash.

```html
<!DOCTYPE html>
<html lang="en">
<head>
<meta charset="utf-8">
<title>CargoLinx – A Multi-Modal Freight Company</title>
<link rel="stylesheet" href="https://fonts.googleapis.com/css2?family=Titillium+Web:wght@400;600;700&family=Arimo:wght@400;700&display=swap">
<style>
:root{
  --red:#9b0f0b;
  --red-dark:#7d0b08;
  --navy:#1d2a47;
  --navy-2:#25355a;
  --page:#efefef;
  --white:#ffffff;
  --body:#3a3a3a;
  --footer:#222222;
  --footer-text:#bdbdbd;
  --footer-head:#dddddd;
}
*{margin:0;padding:0;box-sizing:border-box}
html,body{width:960px;height:1200px;overflow:hidden}
body{background:var(--page);font-family:"Arimo",Arial,sans-serif;color:var(--body);position:relative}
.abs{position:absolute}

/* header */
.site-header{left:0;top:0;width:960px;height:114px;background:#f3f3f3}
.brand{left:80px;top:30px;font-family:"Titillium Web",sans-serif;font-weight:700;font-size:34px;color:var(--navy);letter-spacing:1px;line-height:1}
.tagline{left:81px;top:72px;font-family:"Titillium Web",sans-serif;font-size:16px;color:#333;letter-spacing:.3px}
.social{top:18px;width:29px;height:29px;border-radius:50%;border:2px solid #c9c9c9}
.social.one{left:791px;background:#3b5a9a}
.social.two{left:830px;background:#3fb6e8}
.call-now{right:103px;top:55px;font-family:"Titillium Web",sans-serif;font-size:17px;color:#111}
.call-now span{color:var(--red);font-weight:600}
.email-line{right:103px;top:81px;font-family:"Titillium Web",sans-serif;font-size:15px;color:#222}

/* nav */
.main-nav{left:0;top:114px;width:960px;height:36px;background:var(--red)}
.main-nav a{position:absolute;top:0;height:36px;line-height:36px;font-family:"Titillium Web",sans-serif;font-weight:600;font-size:12.5px;color:var(--white);text-decoration:none}
.nav-sep{position:absolute;top:6px;width:1px;height:24px;background:var(--red-dark);box-shadow:1px 0 0 rgba(255,255,255,.12)}

/* hero */
.hero{left:0;top:150px;width:960px;height:343px;background:
  radial-gradient(ellipse 55% 40% at 48% 45%,rgba(190,32,36,.75),rgba(190,32,36,0) 100%),
  linear-gradient(180deg,#4f76a6 0%,#43699a 45%,#c9d0da 78%,#9fb3cb 100%)}
.arrow{top:290px;width:33px;height:33px;border-radius:50%;background:#000}
.arrow.prev{left:13px}.arrow.next{left:902px}
.caption{left:505px;top:365px;width:373px;height:83px;background:rgba(15,15,15,.82);padding:7px 16px}
.caption h2{font-family:"Titillium Web",sans-serif;font-weight:400;font-size:25px;color:#fff;line-height:1.2}
.caption p{font-family:"Titillium Web",sans-serif;font-size:19px;color:#fff;margin-top:4px;white-space:nowrap}

/* content */
.section-title{font-family:"Titillium Web",sans-serif;font-size:20px;color:var(--navy);font-weight:400}
.about-title{left:79px;top:513px}
.about-text{left:79px;top:555px;width:508px;font-size:10.6px;line-height:14.4px;color:#333}
.about-text p+p{margin-top:14px}
.cta{left:658px;width:222px;height:63px;border-radius:5px;text-align:center;color:#fff;font-family:"Titillium Web",sans-serif}
.cta-quote{top:519px;background:linear-gradient(180deg,var(--navy-2),var(--navy))}
.cta-quote .big{font-weight:700;font-size:25px;line-height:1;padding-top:6px;letter-spacing:1px}
.cta-quote .small{font-size:17px;letter-spacing:1px;margin-top:4px}
.cta-hours{top:598px;background:var(--red)}
.cta-hours .big{font-size:23px;padding-top:6px;line-height:1.1}
.cta-hours .small{font-size:16px;margin-top:2px}
.services-title{left:79px;top:668px}
.service{top:719px;width:189px}
.service h3{height:35px;background:var(--navy);color:#fff;font-family:"Titillium Web",sans-serif;font-weight:600;font-size:11.5px;text-align:center;line-height:35px;white-space:nowrap}
.service .photo{height:107px;box-shadow:0 1px 2px rgba(0,0,0,.35)}
.s1{left:79px}.s1 .photo{background:linear-gradient(180deg,#6fa6db,#caa948 60%,#8a8a80)}
.s2{left:286px}.s2 .photo{background:linear-gradient(180deg,#98a6b8,#e8e8e8 55%,#7c8a6a)}
.s3{left:488px}.s3 .photo{background:linear-gradient(180deg,#8d9a7f,#a7a7a7 45%,#6a7fa9)}
.s4{left:692px}.s4 .photo{background:linear-gradient(180deg,#a9cbe8,#cfdce9 45%,#2d6aa6)}

/* footer */
.site-footer{left:0;top:905px;width:960px;height:213px;background:var(--footer)}
.f-col{top:38px}
.f-col h4{font-size:10.5px;font-weight:700;color:var(--footer-head);letter-spacing:.2px;margin-bottom:11px}
.f-col ul{list-style:none}
.f-col li{font-size:10px;color:var(--footer-text);height:17.6px;position:relative;padding-left:9px;white-space:nowrap}
.f-col li::before{content:"";position:absolute;left:-2px;top:3px;border-left:4px solid #888;border-top:3px solid transparent;border-bottom:3px solid transparent}
.c1{left:81px}.c2{left:289px}.c3{left:506px}.c4{left:720px}
.insurance-band{left:0;top:1118px;width:960px;height:49px;background:var(--navy);text-align:center;color:#c4cad6;font-size:10px;padding-top:9px;line-height:21px}
.copyright{left:0;top:1167px;width:960px;height:33px;background:var(--red);text-align:center;color:#fff;font-size:10px;line-height:29px}
</style>
</head>
<body>

<header class="abs site-header">
  <div class="abs brand">CARGOLINX</div>
  <div class="abs tagline">A MULTI-MODAL FREIGHT COMPANY</div>
  <span class="abs social one" aria-label="Social profile"></span>
  <span class="abs social two" aria-label="Social profile"></span>
  <div class="abs call-now">CALL NOW <span>(555) 014- 2290</span></div>
  <div class="abs email-line">Email us for free qoute : quotes@cargolinx.com</div>
</header>

<nav class="abs main-nav">
  <a style="left:84px">HOME</a>
  <span class="nav-sep" style="left:145px"></span>
  <a style="left:177px">ABOUT US</a>
  <span class="nav-sep" style="left:263px"></span>
  <a style="left:287px">OUR SERVICES</a>
  <span class="nav-sep" style="left:393px"></span>
  <a style="left:422px">INSURANCE &amp; LEGAL INFO</a>
  <span class="nav-sep" style="left:581px"></span>
  <a style="left:619px">FAST FREIGHT QUOTE</a>
  <span class="nav-sep" style="left:761px"></span>
  <a style="left:795px">CONTACT US</a>
</nav>

<section class="abs hero" role="img" aria-label="Container ship loaded with red cargo containers sailing on blue sea"></section>
<div class="abs arrow prev"><svg width="33" height="33" viewBox="0 0 33 33"><path d="M19 10l-7 6.5 7 6.5" stroke="#fff" stroke-width="3" fill="none"/></svg></div>
<div class="abs arrow next"><svg width="33" height="33" viewBox="0 0 33 33"><path d="M14 10l7 6.5-7 6.5" stroke="#fff" stroke-width="3" fill="none"/></svg></div>
<div class="abs caption">
  <h2>Worldwide Shipping</h2>
  <p>Trucking and Ocean Service with No Limits</p>
</div>

<h1 class="abs section-title about-title">ABOUT CARGOLINX</h1>
<div class="abs about-text">
  <p>Welcome to CargoLinx and Meridian Haul Inc. We are a one stop solution logistics company servicing Worldwide with our Trucking and Ocean shipping service.</p>
  <p>In using our freight services, we will negotiate a competitive freight quote using over 5000 different carriers who are certified and contracted by us. We have all equipment types available daily, service all freight types, and have no limits Worldwide.</p>
</div>

<div class="abs cta cta-quote">
  <div class="big">REQUEST A</div>
  <div class="small">FREIGHT QUOTE</div>
</div>
<div class="abs cta cta-hours">
  <div class="big">24 HOURS A DAY</div>
  <div class="small">CALL : (555) 014- 2290</div>
</div>

<h2 class="abs section-title services-title">OUR SERVICES</h2>
<div class="abs service s1"><h3>HEAVY HAUL</h3><div class="photo" role="img" aria-label="Heavy haul truck carrying a large yellow mining dump body"></div></div>
<div class="abs service s2"><h3>DRY &amp; REFRIGERATED</h3><div class="photo" role="img" aria-label="White semi truck with refrigerated trailer"></div></div>
<div class="abs service s3"><h3>FLATBED, STEP DECK &amp; PIGGY BACK</h3><div class="photo" role="img" aria-label="Blue truck pulling a flatbed trailer on a highway"></div></div>
<div class="abs service s4"><h3>FREIGHT FORWARDING OCEAN</h3><div class="photo" role="img" aria-label="Container ship in front of a city skyline with a plane overhead"></div></div>

<footer class="abs site-footer">
  <div class="abs f-col c1"><h4>WORLDWIDE FREIGHT SERVICES</h4><ul>
    <li>Worldwide Shipping Scope</li><li>Trucking Shipping Services</li><li>Ocean Shipping Services</li><li>Insurance &amp; Legal Details</li><li>Get a Freight Quote Now!</li><li>Return to Home Page</li></ul></div>
  <div class="abs f-col c2"><h4>FREIGHT - TRUCKING SERVICE</h4><ul>
    <li>Heavy Equipment Hauling</li><li>LTL Freight Transport</li><li>Flatbed Transport</li><li>Step Deck Transport</li><li>Dry Van Transport</li><li>Refrigerated Transport</li><li>Power Only &amp; Towaway Transport</li></ul></div>
  <div class="abs f-col c3"><h4>OCEAN SHIPPING SERVICES</h4><ul>
    <li>Heavy Equipment Hauling</li><li>LTL Freight Transport</li><li>Flatbed Transport</li><li>Step Deck Transport</li><li>Dry Van Transport</li><li>Refrigerated Transport</li><li>Power Only &amp; Towaway Transport</li></ul></div>
  <div class="abs f-col c4"><h4>WE SHIP IT ALL WORLDWIDE!</h4><ul>
    <li>Full Loads</li><li>LTL-Less Then Full Loads</li><li>Oversized &amp; Overweight Loads</li><li>500 LBS to 200,000 LBS (No Limits)</li><li>Construction &amp; Mining Equipment</li><li>Mills &amp; Machinery</li><li>Hay &amp; Alfalfa</li></ul></div>
</footer>

<div class="abs insurance-band">
  Full Loads, LTL, Oversized Machinery &amp; Equipment. We do it all. All freight covered to full value by our Insurance!<br>
  All freight covered by a minimum of $1,000,000 in Liability and $200,000+ in Cargo Insurance with no limits Worldwide by both Truck and Ocean Carrier Services!
</div>
<div class="abs copyright">2014 Copyright and Owned by Meridian Haul Inc. and CargoLinx.com--Equipment Transport Specialist</div>

</body>
</html>
```